NEW YORK Plumbing/utility company 10 year anniversary business card

Looking For simple back and front business card would like to include a few things in description
We offer 24/7 emergency service
residential
commercial
industrial
municipal
services offered
Plumbing
hydro excavation
hydro jetting
Well pumps
Sewer pumps
water mains
sewer mains

```html
<!DOCTYPE html>
<html lang="en">
<head>
<meta charset="utf-8">
<title>Ridgeline Water &amp; Sewer – Business Card</title>
<link href="https://fonts.googleapis.com/css2?family=Rubik:wght@400;500;600&display=swap" rel="stylesheet">
<style>
  :root {
    --page-bg: #e6e6e6;
    --card-bg: #2b2a29;
    --text-light: #ffffff;
    --accent-red: #e3262b;
    --accent-blue: #29a3dc;
    --brand-grey: #8c8c8c;
    --deco-dark: #141414;
    --deco-mid: #3a3a3a;
  }
  * { margin: 0; padding: 0; box-sizing: border-box; }
  html, body {
    width: 1200px; height: 960px; overflow: hidden;
    background: var(--page-bg);
    font-family: "Rubik", Arial, sans-serif;
    color: var(--text-light);
  }
  .card {
    position: absolute; left: 298px; width: 608px; height: 348px;
    background: var(--card-bg); overflow: hidden;
  }
  .card--front { top: 111px; }
  .card--back { top: 513px; }

  /* Front */
  .sectors {
    position: absolute; top: 29px; left: 0; width: 100%;
    text-align: center; font-size: 15px; letter-spacing: 0.2px;
  }
  .sectors .drop { display: inline-block; width: 8px; height: 11px; margin: 0 3px; vertical-align: -1px; }
  .emergency {
    position: absolute; top: 51px; left: 0; width: 100%;
    text-align: center; font-size: 15px; color: var(--accent-red); font-weight: 500;
  }
  .brand-name {
    color: var(--accent-red); font-weight: 600; text-transform: uppercase;
    line-height: 1.05; letter-spacing: 1px;
  }
  .card--front .brand-name {
    position: absolute; top: 112px; left: 0; width: 100%;
    text-align: center; font-size: 44px;
  }
  .card--front .brand-name small { display: block; font-size: 26px; margin-top: 10px; }
  .services {
    position: absolute; top: 284px; left: 0; width: 100%;
    text-align: center; font-size: 16px; line-height: 20px;
  }
  .services .label { color: var(--accent-blue); font-weight: 500; }
  .services .dot { color: var(--accent-red); margin: 0 4px; font-size: 10px; vertical-align: 2px; }

  /* Back */
  .card--back .brand-name {
    position: absolute; top: 48px; left: 43px; font-size: 34px;
  }
  .card--back .brand-name small { display: block; font-size: 20px; margin-top: 8px; }
  .address {
    position: absolute; top: 201px; left: 43px; font-size: 15px; line-height: 21px;
  }
  .contacts {
    position: absolute; top: 255px; left: 43px; list-style: none;
    font-size: 15px; line-height: 20.5px;
  }
  .contacts li { display: flex; align-items: center; gap: 5px; }
  .contacts svg { width: 13px; height: 13px; }
  .person {
    position: absolute; top: 46px; right: 42px; text-align: right;
  }
  .person-name { color: var(--accent-red); font-size: 19px; font-weight: 500; }
  .person-title { color: var(--accent-blue); font-size: 15px; margin-top: 3px; }
  .brand-decoration {
    position: absolute; left: 334px; top: 99px; width: 274px; height: 249px;
    background: linear-gradient(135deg, var(--deco-mid), var(--deco-dark));
    border-top-left-radius: 4px;
  }
</style>
</head>
<body>

<section class="card card--front">
  <p class="sectors">
    RESIDENTIAL<svg class="drop" viewBox="0 0 8 11"><path d="M4 0 C5 3 8 5 8 7.5 A4 4 0 0 1 0 7.5 C0 5 3 3 4 0Z" fill="#29a3dc"/></svg>COMMERCIAL<svg class="drop" viewBox="0 0 8 11"><path d="M4 0 C5 3 8 5 8 7.5 A4 4 0 0 1 0 7.5 C0 5 3 3 4 0Z" fill="#29a3dc"/></svg>INDUSTRIAL<svg class="drop" viewBox="0 0 8 11"><path d="M4 0 C5 3 8 5 8 7.5 A4 4 0 0 1 0 7.5 C0 5 3 3 4 0Z" fill="#29a3dc"/></svg>MUNICIPAL
  </p>
  <p class="emergency">24/7 Emergency Service</p>
  <h1 class="brand-name">Ridgeline<small>Water &amp; Sewer</small></h1>
  <p class="services">
    <span class="label">Services Offered:</span> Plumbing<span class="dot">•</span>Hydro Excavation<span class="dot">•</span>Hydro Jetting<br>
    Well Pumps<span class="dot">•</span>Sewer Pumps<span class="dot">•</span>Water Mains<span class="dot">•</span>Sewer Mains
  </p>
</section>

<section class="card card--back">
  <h2 class="brand-name">Ridgeline<small>Water &amp; Sewer</small></h2>
  <p class="address">42 Orchard Bend Road<br>Millbrook, NY 12545</p>
  <ul class="contacts">
    <li><svg viewBox="0 0 13 13"><path d="M3 1 L5 4 L4 5.5 C5 7.5 6 8.5 7.5 9 L9 8 L12 10 L11 12 C6 12 1 7 1 2 Z" fill="none" stroke="#29a3dc" stroke-width="1.3" stroke-linejoin="round"/></svg>845-555-0148</li>
    <li><svg viewBox="0 0 13 13"><rect x="1" y="3" width="11" height="8" fill="none" stroke="#29a3dc" stroke-width="1.3"/><path d="M1 3 L6.5 7.5 L12 3" fill="none" stroke="#29a3dc" stroke-width="1.3"/></svg>daniel@ridgelinews.com</li>
    <li><svg viewBox="0 0 13 13"><circle cx="6.5" cy="6.5" r="5.5" fill="none" stroke="#29a3dc" stroke-width="1.2"/><ellipse cx="6.5" cy="6.5" rx="2.4" ry="5.5" fill="none" stroke="#29a3dc" stroke-width="1"/><path d="M1 6.5 H12" stroke="#29a3dc" stroke-width="1"/></svg>www.ridgelinews.com</li>
  </ul>
  <div class="person">
    <p class="person-name">Daniel Brennan</p>
    <p class="person-title">Founder / Owner</p>
  </div>
  <div class="brand-decoration" role="img" aria-label="Large glossy dark brand mark decoration"></div>
</section>

</body>
</html>
```